Brand Business Card for Hotel Cloud Management System

Hello designers,
we are looking for a new brand business card for our product Stayvora. Our brand Stayvora is a hotel management system for small hotels, B&B, guesthouses etc. and just recently we are expanding our offer to other European markets. Therefore we need a business card that will communicate not only to the end-users (hoteliers) but also to potential business partners/ We would like the brand business card to be professional looking, but not too serius, modern, elegant, clean, Our brand color is orange, dark grey and it would be nice to see both combined.

Please visit our website www.stayvora.eu to get more impression on what our brand stayvora stands for.

Please find attached stayvora logo.

Target Market(s)

small hotels, hoteliers, B&B owners, potential business partners

Industry/Entity Type

Software Service

Contact Information for Business Card

Stayvora
- hotel software solutions - web booking engine - multi channel manager
www.stayvora.eu
T: +38614738265
E: info@stayvora.net

Font styles to use
Serif
Sans Serif

Colors
f37122
aaaaaa
606060
f6f6f6

Requirements
Must have
• Logo of the brand
• the layout of the business card should be in connection with the look and feel of the website stayvora.eu and logo stayvora;

```html
<!DOCTYPE html>
<html lang="en">
<head>
<meta charset="utf-8">
<title>Stayvora Business Card</title>
<link href="https://fonts.googleapis.com/css2?family=Fira+Sans:wght@400;500&family=Nunito:wght@800&family=Roboto:wght@400&display=swap" rel="stylesheet">
<style>
  :root {
    --backdrop: #b0b0b0;
    --charcoal: #3f4446;
    --orange: #e36714;
    --white: #ffffff;
  }
  html, body {
    margin: 0;
    padding: 0;
    overflow: hidden;
  }
  .canvas {
    position: relative;
    width: 1200px;
    height: 751px;
    background: var(--backdrop);
    overflow: hidden;
  }
  .hangers {
    position: absolute;
    inset: 0;
  }
  .hanger-front { fill: var(--charcoal); }
  .hanger-back { fill: var(--orange); }

  .brand {
    position: absolute;
    left: 246px;
    width: 332px;
    top: 524px;
    text-align: center;
    color: var(--white);
  }
  .brand-name {
    display: inline-flex;
    align-items: center;
    gap: 8px;
    font-family: "Nunito", sans-serif;
    font-weight: 800;
    font-size: 44px;
    line-height: 1;
    letter-spacing: -0.5px;
  }
  .brand-dot {
    width: 14px;
    height: 14px;
    border-radius: 50%;
    background: var(--orange);
  }
  .brand-tagline {
    margin-top: 4px;
    font-family: "Fira Sans", sans-serif;
    font-size: 14px;
    line-height: 1.2;
  }

  .contact-card {
    position: absolute;
    left: 672px;
    top: 455px;
    color: var(--white);
  }
  .person-name {
    margin: 0;
    font-family: "Fira Sans", sans-serif;
    font-weight: 500;
    font-size: 22px;
    line-height: 1.2;
  }
  .person-role {
    margin: 2px 0 0;
    font-family: "Fira Sans", sans-serif;
    font-size: 14.5px;
  }
  .contact-list {
    list-style: none;
    margin: 40px 0 0;
    padding: 0;
    font-family: "Roboto", sans-serif;
    font-size: 15px;
  }
  .contact-list li {
    display: flex;
    align-items: center;
    height: 21px;
  }
  .contact-icon {
    width: 12px;
    height: 12px;
    margin-right: 15px;
    fill: var(--white);
  }
</style>
</head>
<body>
<div class="canvas">
  <svg class="hangers" viewBox="0 0 1500 938" width="1200" height="751" aria-hidden="true">
    <defs>
      <path id="hanger-shape" d="M370 120 H665 Q723 120 723 180 V758 Q723 818 663 818 H368 Q308 818 308 758 V600 C308 520 330 480 420 465 C520 445 620 440 625 330 C625 260 575 213 515 213 C460 213 440 260 420 300 C400 345 380 362 350 362 C325 362 308 340 308 310 V180 Q308 120 370 120 Z"/>
    </defs>
    <use href="#hanger-shape" class="hanger-front"/>
    <use href="#hanger-shape" class="hanger-back" transform="translate(1498 0) scale(-1 1)"/>
  </svg>

  <div class="brand">
    <div class="brand-name"><span class="brand-dot"></span>Stayvora</div>
    <div class="brand-tagline">hotel pms service</div>
  </div>

  <div class="contact-card">
    <p class="person-name">John Doe Smith</p>
    <p class="person-role">Managing Director</p>
    <ul class="contact-list">
      <li>
        <svg class="contact-icon" viewBox="0 0 12 12"><path d="M1 4 Q6 0 11 4 L9.5 5.5 L8 4.5 V3.8 Q6 3 4 3.8 V4.5 L2.5 5.5 Z M3 6 H9 L10.5 11 H1.5 Z"/></svg>
        +38614738265
      </li>
      <li>
        <svg class="contact-icon" viewBox="0 0 12 12"><path d="M0 2 H12 V10 H0 Z M1 3 L6 7 L11 3 V3 Z" fill-rule="evenodd"/></svg>
        info@stayvora.net
      </li>
      <li>
        <svg class="contact-icon" viewBox="0 0 12 12"><circle cx="6" cy="6" r="5.2" fill="none" stroke="#fff" stroke-width="1.2"/><path d="M0.8 6 H11.2 M6 0.8 V11.2" stroke="#fff" stroke-width="1"/><ellipse cx="6" cy="6" rx="2.3" ry="5.2" fill="none" stroke="#fff" stroke-width="1"/></svg>
        www.stayvora.eu
      </li>
    </ul>
  </div>
</div>
</body>
</html>
```